依頼詳細
高級住宅地、オフィス街を対象に配るA4チラシ(片面)になります。高級感溢れるデザインをお願いいたします。
印刷はミドリカゼを使用する予定です。入稿可能なAiファイルでの作成をお願いいたします。
https://midorikaze-example.jp/dataguide/

色選びはカラーパレットをご使用ください。
記載項目
記載内容は添付のワードファイルをご参照ください。
講師プロフィール用の写真は仮の写真です。決定いたしまた方に後ほど実際に使用いただく写真をお渡しいたします。
イメージ画像を1枚添付しておりますが、使用はお任せいたします。
サイズ
A4
ページ数
片面
希望イメージ
シンプル 複雑
単色 カラフル
暗い 明るい
日常 高級
遊び心 厳粛
未来的 伝統的
女性的 男性的
希望する色
黄・オレンジ系、青系、無彩色系
納品ファイル
• イラストレーター形式 (.ai)
補足説明
当初の設定ミスで募集期間5日間としていましたが、3日間に訂正いたします。
期間が短くなりますが、どうぞよろしくお願いいたします。
報酬金額変更いたしました。
どうぞよろしくお願いいたします。
提出ファイル形式についての追記です。
採用に至った場合は、そのまま入稿できるAiファイルと後に文字を編集する予定があるためテキストをアウトライン化する前(テキスト部分が後に編集できるもの)のファイルの2種類の提出をお願いいたします。可能であればWindows Adobe Illustrator CS4対応のファイル形式でお願いします。また、特殊なフォントをご使用の場合は一緒にご提出願います。
お手数おかけいたしますがよろしくお願いいたします。

ターゲットを意識した画像の使用、レイアウト、高級感とすべてよかったです。

この度はコンペにご参加いただきありがとうございました。
予想以上に多くの提案をいただきまして大変感謝いたしております。
多数の素晴らしいご提案から選ぶのに時間がかかりまして、
お待たせいたしましたことをお詫び申し上げます。
また、機会がございましたらどうぞよろしくお願いいたします。

```html
<!DOCTYPE html>
<html lang="ja">
<head>
<meta charset="utf-8">
<title>LUXE プライベート英会話レッスン</title>
<link rel="stylesheet" href="https://fonts.googleapis.com/css2?family=Shippori+Mincho:wght@500;700;800&family=Noto+Sans+JP:wght@400;700&family=Cormorant+Garamond:ital,wght@0,600;1,600&display=swap">
<style>
:root{
  --ink:#0b0b0c;
  --gold:#c9a24e;
  --gold-light:#e6cc8a;
  --text:#f3efe6;
  --muted:#b9b3a6;
  --red:#c0392b;
}
*{margin:0;padding:0;box-sizing:border-box}
html,body{width:849px;height:1200px;overflow:hidden;background:var(--ink)}
body{font-family:"Noto Sans JP",sans-serif;color:var(--text);position:relative}
.skyline{position:absolute;left:0;top:0;width:849px;height:1150px;
  background:radial-gradient(ellipse at 80% 18%,rgba(120,110,90,.45),transparent 55%),
             radial-gradient(ellipse at 80% 45%,rgba(90,90,100,.35),transparent 60%),
             linear-gradient(180deg,#121214 0%,#1b1b1f 45%,#101012 100%)}
.abs{position:absolute}
.title{left:0;top:14px;width:849px;text-align:center;font-family:"Shippori Mincho",serif;font-weight:800;font-size:29px;color:var(--gold-light);letter-spacing:1px;white-space:nowrap}
.title .brand{font-size:20px;margin-left:14px;color:var(--gold)}
.subtitle{left:0;top:56px;width:849px;text-align:center;font-family:"Shippori Mincho",serif;font-size:15px}
.rule{left:30px;width:789px;height:1px;background:var(--gold)}
.intro{left:34px;top:98px;width:520px;font-family:"Shippori Mincho",serif;font-size:16px;line-height:1.75;white-space:nowrap}
.note-box{left:565px;top:160px;width:255px;padding:7px 10px;border:1px solid var(--gold);font-size:10.5px;line-height:1.55;background:rgba(0,0,0,.5)}
.limited{left:28px;top:226px;width:76px;height:76px;border-radius:50%;background:var(--gold);color:var(--ink);display:flex;align-items:center;justify-content:center;font-family:"Shippori Mincho",serif;font-weight:800;font-size:15px;text-align:center;line-height:1.2}
.limited-copy{left:124px;top:224px;font-family:"Shippori Mincho",serif;font-size:14px;line-height:1.7;white-space:nowrap}
.slot{left:124px;top:270px;font-family:"Shippori Mincho",serif;font-weight:800;font-size:28px;line-height:1.2;color:var(--gold-light);white-space:nowrap}
.slot small{font-size:18px;margin-right:8px}
.card{background:rgba(20,20,22,.88);border:1px solid var(--gold)}
.card h2{font-family:"Shippori Mincho",serif;font-size:15px;color:var(--gold-light);padding:7px 12px;border-bottom:1px solid var(--gold);white-space:nowrap}
.reasons{left:18px;top:320px;width:425px;height:305px}
.reasons ul{list-style:none;padding:10px 14px;font-size:11.5px;line-height:1.55}
.reasons li{margin-bottom:8px;padding-left:14px;position:relative}
.reasons li::before{content:"■";position:absolute;left:0;color:var(--gold);font-size:9px;top:2px}
.reasons li span{display:block;color:var(--muted);font-size:10px}
.lesson{left:455px;top:320px;width:190px;height:250px}
.lesson .body{padding:8px 10px;font-size:10.5px;line-height:1.5}
.lesson .lead{font-size:12px;font-weight:700;margin-bottom:4px}
.lesson dt{color:var(--gold-light);font-weight:700;margin-top:3px}
.profile{left:18px;top:645px;width:640px;height:250px}
.portrait{position:absolute;left:12px;top:46px;width:120px;height:160px;background:linear-gradient(160deg,#8a8478,#4b4740)}
.profile .text{position:absolute;left:146px;top:46px;width:478px;font-size:11px;line-height:1.7}
.goal{left:680px;top:700px;width:155px;height:155px;border-radius:50%;background:radial-gradient(circle,#f5efe0,#d9c9a1);color:var(--ink);display:flex;align-items:center;justify-content:center;text-align:center;font-family:"Shippori Mincho",serif;font-weight:700;font-size:12.5px;line-height:1.6}
.quote{left:0;top:905px;width:849px;text-align:center;font-family:"Cormorant Garamond",serif;font-style:italic;font-size:21px;color:var(--gold-light);white-space:nowrap}
.message{left:28px;top:950px;width:500px;font-size:11.5px;line-height:1.8}
.price{left:552px;top:945px;width:268px;height:170px}
.price .body{padding:12px 14px;font-size:13px;line-height:1.9}
.price b{font-family:"Shippori Mincho",serif;font-size:20px;color:var(--gold-light)}
.price small{font-size:10px;color:var(--muted);display:block;line-height:1.3}
.footer{left:0;top:1155px;width:849px;height:45px;background:var(--text);color:var(--ink);display:flex;align-items:center;justify-content:space-around;font-size:13px;font-weight:700}
.footer .red{color:var(--red)}
</style>
</head>
<body>
<div class="skyline" role="img" aria-label="夜景の高層ビル街の写真"></div>

<h1 class="abs title">ワンランク上の完全プライベート英会話レッスン<span class="brand">LUXE</span></h1>
<p class="abs subtitle">— 全てにおいて最高品質を求める貴方へ —</p>
<div class="abs rule" style="top:86px"></div>

<p class="abs intro">LUXEは、経営者、会社役員、議員、医師、ニュースキャスターなど<br>エリートの皆様御用達の特別な英会話レッスンです。<br>福岡市内のご自宅や職場など、お客様のご希望の場所で<br>洗練されたプライベートレッスンを提供しています。</p>
<div class="abs note-box">福岡市内で屈指の英会話レッスン。第一線で活躍するお客様に選ばれ続けています。講師は20年以上の指導経験があります。</div>

<div class="abs limited">限定<br>案内</div>
<p class="abs limited-copy">エグゼクティブの方々から大好評をいただいております。<br>ジョン・グレイ（LUXE代表講師）のレッスンに枠空きが生まれました。</p>
<p class="abs slot"><small>火曜日</small>19:00－20:00</p>

<section class="abs card reasons">
  <h2>なぜ、ジョンのレッスンはそんなに人気なのか？</h2>
  <ul>
    <li>ジョンは豊富なビジネス経験を持つプロフェッショナルです。<span>（多くの業界での実務経験）</span></li>
    <li>ジョンのレッスンは単に「英語を学ぶだけ」ではありません。<span>ビジネスの場で使える表現と考え方を身につけ、国際的な交渉にも対応できます。</span></li>
    <li>既存の退屈な教材は使用しません。<span>お客様の目標に合わせて、毎回オリジナルの内容をご用意します。</span></li>
    <li>レッスンを受けるだけでお客様の英語は上達します。<span>確かな成果を実感いただけるよう丁寧に指導します。</span></li>
  </ul>
</section>

<section class="abs card lesson">
  <h2>レッスン案内</h2>
  <div class="body">
    <p class="lead">1回60分のレッスンです。</p>
    <dl>
      <dt>日時</dt><dd>毎週火曜日 19:00～20:00</dd>
      <dt>内容</dt><dd>会話・発音・ビジネス表現など</dd>
      <dt>場所</dt><dd>福岡市内のご希望の場所</dd>
      <dt>特典</dt><dd>30分の面接＋英語力診断<br>（5,000円相当）</dd>
    </dl>
  </div>
</section>

<section class="abs card profile">
  <h2>講師：ジョン・グレイ紹介</h2>
  <div class="portrait" role="img" aria-label="講師の写真"></div>
  <p class="text">英国出身、福岡在住20年。大学で経営学を修め、国際企業での勤務を経て英会話講師に。経営者や医師など多くのエグゼクティブを指導してきました。ビジネス英語、プレゼンテーション、交渉術の指導に定評があり、日本文化への深い理解をもとに、お客様一人ひとりに合ったレッスンを提供しています。英語教育の資格も複数保有しています。</p>
</section>

<div class="abs goal">私のゴールは、<br>一人でも多くの<br>日本人に英語を<br>身につけて<br>もらうこと</div>

<p class="abs quote">“My goal is to make the country of Japan stronger, one person at a time.”</p>

<p class="abs message">日本が国際社会の中でさらに輝くためには、英語で発信できる人材が欠かせません。私はこれまで多くの方の挑戦を支えてきました。実践的なレッスンを通じて、自信を持って世界と向き合える力を身につけていただきます。皆様とお会いできることを楽しみにしております。</p>

<section class="abs card price">
  <h2>料金</h2>
  <div class="body">
    <p>初回試験料 <b>5,000円</b><small>（税込・面接含む）</small></p>
    <p>レッスン料 <b>25,000円</b>/60分<small>（税込・交通費込み）</small></p>
  </div>
</section>

<footer class="abs footer">
  <span>お問い合わせ</span>
  <span>Email: info@luxe-lesson.jp</span>
  <span class="red">電話：092-000-1234</span>
  <span>携帯：080-0000-5678</span>
</footer>
</body>
</html>
```